Book Cover Design Project

I am writing a book called Sisters & Figs. It may be a combination of traditional publishing, an ebook, and/or self-publishing. This will be the first book in a series of 4 books. The audience are 50ish women (40 year olds will probably read it to) who are successful, accomplished and who have made lemonade out of lemons in life, and now I am encouraging them to take that lemon in hand and instead of making lemonade, squeeze the life out of that lemon and get the zest that life still has to offer them. "Rise Up Today" is a subtitle of the book. From the book cover design, I also hope to derive a logo for journals and a T-Shirt design that rocks. These women are sexy, sassy, smart, and sensational and are looking for the adventure that life has to offer them, not rocking chairs. So for a design I am looking for it to incorporate women, a woman's hand squeezing a lemon, maybe lots of lemons, lots of yellow, squeezing a lemon, squeezing life, fun, adventure and excitement in the book cover design. I want it to POP right off the book and WOW women so that the book will scream "buy me" just because of the cover and be surprised to the content it has to offer. I am looking for absolutely spectacular cover that is absolutely sensational. I am hoping to use the same person for the logo, so keep that in mind.

Target Market(s)

women 40 - 60

Industry/Entity Type

Publishing

Requirements
Must have
• Women, Lemons, Excitement, Sexy, Classy, Sensational, the color yellow
Nice to have
• maybe the hand of a woman squeezing a lemon and juice coming out

maybe a woman, several, or a group of women in a barrel, pool or mansion full of lemons

```html
<!DOCTYPE html>
<html lang="en">
<head>
<meta charset="utf-8">
<title>Sisters and Figs – Book Cover</title>
<link rel="stylesheet" href="https://fonts.googleapis.com/css2?family=Anton&family=Archivo+Black&family=Cinzel:wght@500;700&family=Homemade+Apple&display=swap">
<style>
  :root {
    --page: #ffffff;
    --band: #fdd835;
    --band-edge: #ffeb3b;
    --ink: #111111;
    --accent-red: #ff0000;
    --magenta: #e51ff2;
    --gold: #f0c419;
    --rule: #b9b9b9;
  }
  html, body {
    margin: 0;
    width: 1000px;
    height: 1200px;
    overflow: hidden;
    background: var(--page);
  }
  .cover {
    display: block;
    width: 1000px;
    height: 1200px;
  }
  .author-band { fill: var(--band); }
  .author-band-edge { fill: var(--band-edge); }
  .author-name {
    font-family: 'Cinzel', serif;
    font-weight: 700;
    font-size: 54px;
    fill: var(--ink);
  }
  .title-word {
    font-family: 'Anton', sans-serif;
    font-size: 330px;
    stroke-width: 5;
    paint-order: stroke;
  }
  .title-top { stroke: var(--magenta); }
  .title-bottom { stroke: var(--gold); }
  .connector {
    font-family: 'Archivo Black', sans-serif;
    font-size: 66px;
    fill: var(--ink);
  }
  .rule { fill: var(--rule); }
  .subtitle {
    font-family: 'Cinzel', serif;
    font-weight: 700;
    font-size: 44px;
    fill: var(--ink);
  }
  .subtitle .emphasis {
    fill: var(--accent-red);
    font-family: 'Cinzel', serif;
  }
  .tagline {
    font-family: 'Homemade Apple', cursive;
    font-size: 54px;
    fill: var(--ink);
  }
</style>
</head>
<body>
<svg class="cover" viewBox="0 0 1000 1200" xmlns="http://www.w3.org/2000/svg">
  <defs>
    <linearGradient id="portrait-tones" x1="0" y1="0" x2="1" y2="0">
      <stop offset="0" stop-color="#d9d6d2"/>
      <stop offset="0.12" stop-color="#5e5853"/>
      <stop offset="0.3" stop-color="#8a7f76"/>
      <stop offset="0.4" stop-color="#6e4b35"/>
      <stop offset="0.55" stop-color="#b9a79a"/>
      <stop offset="0.75" stop-color="#d8d8d4"/>
      <stop offset="1" stop-color="#ecece8"/>
    </linearGradient>
    <linearGradient id="fruit-splash-tones" x1="0" y1="0" x2="0" y2="1">
      <stop offset="0" stop-color="#ffffff"/>
      <stop offset="0.16" stop-color="#ffffff"/>
      <stop offset="0.2" stop-color="#5f6a4e"/>
      <stop offset="0.35" stop-color="#b8c24a"/>
      <stop offset="0.6" stop-color="#f2e236"/>
      <stop offset="0.85" stop-color="#f7ee9a"/>
      <stop offset="1" stop-color="#ffffff"/>
    </linearGradient>
  </defs>

  <rect x="0" y="0" width="1000" height="1200" fill="var(--page)"/>

  <g class="author-block">
    <rect class="author-band" x="153" y="42" width="740" height="88"/>
    <rect class="author-band-edge" x="153" y="130" width="740" height="8"/>
    <text class="author-name" x="505" y="110" text-anchor="middle">AUTHOR’S NAME</text>
  </g>

  <g class="title-top-group" role="img" aria-label="Photo of a woman with long hair lifting her face to the sky, seen through the letters">
    <text class="title-word title-top" x="205" y="426" textLength="628" lengthAdjust="spacingAndGlyphs" fill="url(#portrait-tones)">SISTERS</text>
  </g>

  <g class="connector-group">
    <rect class="rule" x="195" y="510" width="262" height="5" rx="2.5"/>
    <rect class="rule" x="598" y="510" width="257" height="5" rx="2.5"/>
    <text class="connector" x="526" y="530" text-anchor="middle">and</text>
  </g>

  <g class="title-bottom-group" role="img" aria-label="Photo of fruit slices splashing into clear water, seen through the letters">
    <text class="title-word title-bottom" x="205" y="836" textLength="650" lengthAdjust="spacingAndGlyphs" fill="url(#fruit-splash-tones)">FIGS</text>
  </g>

  <text class="subtitle" x="525" y="925" text-anchor="middle">Being <tspan class="emphasis">YOUR</tspan> Adventure</text>

  <text class="tagline" x="850" y="1068" text-anchor="end">Live your dreams</text>
</svg>
</body>
</html>
```